Hydrographic business needs a business card that reaches hunters and off-road enthusiasts

We need a business card for a new hydrographics company catering to customers such as hunters, off-road ATV riders and custom vehicle enthusiasts. A western theme is preferred but professional. Our service should be thought of as upper end graphic design on firearms, off road vehicles, motorcycles, etc... See www.caldorfx.com for ideas on patterns, colors, etc...

Target Market(s)

Hunters, off road enthusiasts, custom car enthusiasts, motorcycle riders...

Industry/Entity Type

Graphic Design

```html
<!DOCTYPE html>
<html lang="en">
<head>
<meta charset="utf-8">
<title>Caldor Surface Works – Business Card</title>
<link rel="stylesheet" href="https://fonts.googleapis.com/css2?family=Open+Sans:wght@400;600;700&display=swap">
<style>
  :root {
    --page-bg: #e8e3db;
    --red-dark: #7d0f15;
    --red: #a8181f;
    --red-light: #b8242b;
    --band-black: #0c0c0c;
    --band-black-edge: #2a2a2a;
    --band-white: #f7f7f7;
    --band-white-edge: #d6d6d6;
    --ink-light: #ffffff;
    --ink-soft: #f1d9da;
    --ink-dark: #1c1c1c;
  }
  * { margin: 0; padding: 0; box-sizing: border-box; }
  html, body {
    width: 1200px; height: 1023px; overflow: hidden;
    background: var(--page-bg);
    font-family: "Open Sans", Arial, sans-serif;
  }
  .sheet {
    width: 1200px; height: 1023px;
    display: flex; align-items: center; justify-content: center; gap: 40px;
  }
  .card {
    width: 560px; height: 320px;
    border-radius: 4px;
    overflow: hidden;
    position: relative;
    box-shadow: 0 10px 26px rgba(0,0,0,.28);
  }
  /* Front */
  .card--front { display: flex; flex-direction: column; }
  .front__head {
    height: 135px;
    background: linear-gradient(160deg, var(--red-light), var(--red) 45%, var(--red-dark));
    padding: 28px 30px 0;
  }
  .brand-name {
    font-family: "Open Sans", Arial, sans-serif;
    font-weight: 600;
    font-size: 40px; line-height: 1.1;
    color: var(--ink-light);
  }
  .tagline {
    margin-top: 12px;
    font-size: 14px; color: var(--ink-soft);
  }
  .front__name-band {
    height: 36px;
    background: linear-gradient(180deg, var(--band-black-edge), var(--band-black) 40%, var(--band-black));
    display: flex; align-items: center; justify-content: center;
    color: var(--ink-light); font-size: 16px;
  }
  .person { font-weight: 700; }
  .divider { margin: 0 8px; opacity: .8; }
  .role { font-weight: 400; font-size: 14px; }
  .front__contact-band {
    height: 66px;
    background: linear-gradient(180deg, var(--band-white-edge), var(--band-white) 25%, var(--band-white) 75%, var(--band-white-edge));
    display: flex; flex-direction: column; justify-content: center; align-items: center; gap: 5px;
    font-size: 13px; color: var(--ink-dark);
  }
  .contact-line { display: flex; align-items: center; gap: 7px; width: 170px; }
  .contact-line svg { width: 12px; height: 12px; fill: var(--ink-dark); flex: none; }
  .front__footer {
    flex: 1;
    background: linear-gradient(160deg, var(--red), var(--red-dark));
    display: flex; flex-direction: column; justify-content: center; align-items: center; gap: 4px;
    color: var(--ink-soft);
  }
  .footer-company { font-size: 13px; }
  .footer-address { font-size: 14px; }
  /* Back */
  .card--back {
    background: radial-gradient(ellipse at 40% 35%, var(--red-light), var(--red) 45%, var(--red-dark));
    display: flex; align-items: center; justify-content: center;
  }
  .back__brand {
    font-family: "Open Sans", Arial, sans-serif;
    font-weight: 600;
    font-size: 38px; color: var(--ink-light);
  }
</style>
</head>
<body>
<main class="sheet">
  <section class="card card--front">
    <header class="front__head">
      <h1 class="brand-name">Caldor Surface Works</h1>
      <p class="tagline">the best and most reliable hydrographics service in East Texas</p>
    </header>
    <div class="front__name-band">
      <span class="person">Wade Calloway</span><span class="divider">|</span><span class="role">Owner</span>
    </div>
    <div class="front__contact-band">
      <p class="contact-line">
        <svg viewBox="0 0 24 24" aria-hidden="true"><path d="M6.6 10.8a15.1 15.1 0 0 0 6.6 6.6l2.2-2.2a1 1 0 0 1 1-.25 11.4 11.4 0 0 0 3.6.57 1 1 0 0 1 1 1V20a1 1 0 0 1-1 1A17 17 0 0 1 3 4a1 1 0 0 1 1-1h3.5a1 1 0 0 1 1 1c0 1.25.2 2.45.57 3.57a1 1 0 0 1-.25 1z"/></svg>
        (555) 014-2290
      </p>
      <p class="contact-line">
        <svg viewBox="0 0 24 24" aria-hidden="true"><path d="M2 5h20v14H2z M4 7v.4l8 5.2 8-5.2V7z" fill-rule="evenodd"/></svg>
        hello@caldorfx.com
      </p>
    </div>
    <footer class="front__footer">
      <p class="footer-company">Caldor Surface Works</p>
      <p class="footer-address">212 Mesa Ridge Road 40, Red Hollow, TX, United States</p>
    </footer>
  </section>

  <section class="card card--back">
    <p class="back__brand">Caldor Surface Works</p>
  </section>
</main>
</body>
</html>
```